Business Card design for amazing new Dental Office

Please read this brief closely!

Our client is a modern new dental office/
They love their new logo.
Now it's time to create a business card for them.

It should be a two sided card:
Side one should have the logo and name and maybe a color background or design.
Side two should have all the contact information which is here:

Marcus Pellow, D.D.S
General and Cosmetic Dentistry
4178 W. Orchard Lane
Dunmere Bay, OR 97120
(541) 219-4862
drmarc@bluefernsmiles.example
www.bluefernsmiles.example

Feel free to arrange that info as you like and to style both sides of the card according to your creativity. This is a chance for you to show your design skills!

Client is open to font choices and is looking for a style that is amazing and premium. Colors can be selected from the logo, or any variation of those.

You will not win this contest with a less than beautiful card design so please feel free to make multiple submissions.

Logo files attached and please message me with any questions.
Thanks!

Target Market(s)

Families and Professionals seeking dental services

Industry/Entity Type

Dental

Contact Information for Business Card

Logo, style, contact info as per the brief

Font styles to use
Sans Serif

Requirements
Must have
• Client's logo and contact details as per brief
Nice to have
• Unique style reflecting high end dental clinic near the beach
Should not have
• Must not look like a template

```html
<!DOCTYPE html>
<html lang="en">
<head>
<meta charset="utf-8">
<title>Blue Fern Smiles – Business Card</title>
<link rel="stylesheet" href="https://fonts.googleapis.com/css2?family=Arimo:wght@400;700&family=Josefin+Sans:wght@400&display=swap">
<style>
  :root {
    --backdrop: #e9e9e7;
    --paper: #f7f7f6;
    --ink-dark: #1f1f20;
    --ink-dark-edge: #2c2c2e;
    --brand-blue: #2f9fe0;
    --brand-teal: #5bb8b4;
    --brand-gold: #d9b33a;
    --text-grey: #8f9090;
    --rule-grey: #b5b5b5;
    --logo-grey: #9a9a9a;
    --white: #ffffff;
  }
  * { box-sizing: border-box; margin: 0; padding: 0; }
  html, body {
    width: 1200px; height: 801px; overflow: hidden;
    background: var(--backdrop);
  }
  .canvas {
    position: relative; width: 1200px; height: 801px;
    display: flex; align-items: center; justify-content: center; gap: 60px;
  }
  .card {
    position: relative; width: 525px; height: 300px;
    border-radius: 3px; overflow: hidden;
    box-shadow: 0 10px 30px rgba(0,0,0,0.14), 0 2px 6px rgba(0,0,0,0.08);
  }

  /* Contact side */
  .card--contact { background: var(--paper); }
  .brand-lockup {
    position: absolute; left: 40px; top: 78px; width: 190px;
    display: flex; align-items: center; gap: 10px;
  }
  .brand-lockup__dot {
    width: 22px; height: 22px; border-radius: 50%;
    background: var(--brand-gold); flex: none;
  }
  .brand-lockup__name {
    font-family: "Josefin Sans", sans-serif; font-weight: 400;
    font-size: 25px; line-height: 1.1; letter-spacing: 1.5px;
    text-transform: uppercase; color: var(--logo-grey);
  }
  .divider {
    position: absolute; left: 243px; top: 48px; width: 1px; height: 108px;
    background: var(--rule-grey);
  }
  .contact {
    position: absolute; left: 262px; top: 44px;
    font-family: "Arimo", sans-serif; color: var(--text-grey);
  }
  .contact__name {
    font-weight: 700; font-size: 19px; color: var(--brand-blue); letter-spacing: 0.2px;
  }
  .contact__title { font-size: 13px; margin-top: 3px; }
  .contact__list { list-style: none; margin-top: 12px; }
  .contact__item {
    display: flex; align-items: center; gap: 8px;
    font-size: 13px; line-height: 19px;
  }
  .contact__icon { width: 12px; height: 12px; flex: none; fill: var(--brand-blue); }
  .wave-band {
    position: absolute; left: 0; right: 0; top: 196px; height: 34px;
    background: linear-gradient(90deg, var(--brand-teal), var(--brand-blue));
    opacity: 0.85;
  }
  .address {
    position: absolute; right: 32px; top: 246px;
    font-family: "Arimo", sans-serif; font-size: 13px; color: var(--text-grey);
  }

  /* Brand side */
  .card--brand {
    background: radial-gradient(ellipse at 60% 45%, var(--ink-dark-edge), var(--ink-dark) 75%);
  }
  .emboss-pattern {
    position: absolute; inset: 0;
    background: linear-gradient(135deg, rgba(255,255,255,0.05), rgba(0,0,0,0.12));
  }
  .brand-mark {
    position: absolute; right: 40px; top: 128px;
    display: flex; align-items: center; gap: 12px;
  }
  .brand-mark__dot {
    width: 24px; height: 24px; border-radius: 50%; background: var(--brand-gold);
  }
  .brand-mark__name {
    font-family: "Josefin Sans", sans-serif; font-weight: 400;
    font-size: 28px; letter-spacing: 2px; text-transform: uppercase;
    color: var(--white);
  }
</style>
</head>
<body>
<main class="canvas">

  <section class="card card--contact" aria-label="Business card, contact side">
    <div class="brand-lockup">
      <span class="brand-lockup__dot"></span>
      <span class="brand-lockup__name">Blue Fern Smiles</span>
    </div>
    <div class="divider"></div>
    <div class="contact">
      <p class="contact__name">Marcus Pellow, D.D.S</p>
      <p class="contact__title">General and Cosmetic Dentistry</p>
      <ul class="contact__list">
        <li class="contact__item">
          <svg class="contact__icon" viewBox="0 0 24 24" aria-hidden="true"><path d="M6.6 10.8a15.1 15.1 0 0 0 6.6 6.6l2.2-2.2c.3-.3.7-.4 1-.2 1.1.4 2.3.6 3.6.6.6 0 1 .4 1 1V20c0 .6-.4 1-1 1A17 17 0 0 1 3 4c0-.6.4-1 1-1h3.5c.6 0 1 .4 1 1 0 1.3.2 2.5.6 3.6.1.3 0 .7-.2 1z"/></svg>
          (541) 219-4862
        </li>
        <li class="contact__item">
          <svg class="contact__icon" viewBox="0 0 24 24" aria-hidden="true"><path d="M2 5h20v14H2z M2 5l10 8 10-8" fill="var(--brand-blue)" stroke="var(--paper)" stroke-width="1.5"/></svg>
          drmarc@bluefernsmiles.example
        </li>
        <li class="contact__item">
          <svg class="contact__icon" viewBox="0 0 24 24" aria-hidden="true"><circle cx="12" cy="12" r="10"/><path d="M2 12h20M12 2c3 3 3 17 0 20M12 2c-3 3-3 17 0 20" fill="none" stroke="var(--paper)" stroke-width="1.5"/></svg>
          www.bluefernsmiles.example
        </li>
      </ul>
    </div>
    <div class="wave-band" role="img" aria-label="Decorative band of flowing teal and blue waves"></div>
    <p class="address">4178 W. Orchard Lane, Dunmere Bay, OR 97120</p>
  </section>

  <section class="card card--brand" aria-label="Business card, brand side">
    <div class="emboss-pattern" role="img" aria-label="Tone-on-tone embossed wave pattern across the black card"></div>
    <div class="brand-mark">
      <span class="brand-mark__dot"></span>
      <span class="brand-mark__name">Blue Fern Smiles</span>
    </div>
  </section>

</main>
</body>
</html>
```